Harbor Parcelworks Advertising Flyers

Our logistical company handles purchasing, receiving, and shipment of goods to the Bahamas and we would like to start our marketing and advertising push. The company will also deliver items to clients as well, similar to an Brivora type of experience. We already have our logo designed and we would like to setup our advertising look and feel for our flyers and banner ads. I would like design templates for:
Full Page Flyer: 8.5 in. X 11 in. (width x height) in PDF
Social Media 1: 1080 px x 1350 px (width x height) in JPG or PNG
Social Media 2: 1080 px X 1080 px (width x height) in JPG or PNG
I would like all the PSD files and the information for all fonts used within all the designs as well. I'm sharing our logo and font files for incorporating into the design and for branding.
For design references that we like please review the attached folder with design examples for reference.
The call to action on the flyer/banners should be:
Company Address:
517 NE 46th Lane, Ft. Lauderdale, Florida 33308
Email: Harbor618@mailvane.com
Website: Harbor618.com
We just need them for placeholders and we can add more contact information once the design concepts are confirmed.

Target Market(s)

Persons buying goods online and needing them shipped to them.

Requirements
Must have
• Designs should have strong design elements and be easy to adjust or tweak with copy if necessary.
Nice to have
• I provided examples of designs we like but it doesn't have to be exact.

```html
<!DOCTYPE html>
<html lang="en">
<head>
<meta charset="utf-8">
<title>Harbor Parcelworks Flyer</title>
<link rel="stylesheet" href="https://fonts.googleapis.com/css2?family=Orbitron:wght@500;700&family=Fira+Sans:wght@400;700;800&family=Montserrat:wght@400;500;800&display=swap">
<style>
  :root {
    --navy: #2b2468;
    --green: #8cc63f;
    --paper: #ffffff;
    --mist: #eef0f2;
    --ink: #2a2a2a;
    --table: #e4e5e7;
  }
  * { box-sizing: border-box; margin: 0; padding: 0; }
  html, body { width: 1200px; height: 1128px; overflow: hidden; background: var(--table); }
  .flyer {
    position: absolute; left: 179px; top: 19px; width: 842px; height: 1090px;
    background: var(--paper); overflow: hidden;
    box-shadow: 0 6px 24px rgba(0,0,0,.18);
    font-family: "Montserrat", sans-serif; color: var(--ink);
  }
  .flyer-shapes { position: absolute; inset: 0; }
  .abs { position: absolute; }
  .brand {
    left: 30px; top: 68px; display: flex; align-items: center; gap: 12px;
    font-family: "Orbitron", sans-serif; font-weight: 700; font-size: 25px;
    color: var(--navy); letter-spacing: 1px; text-transform: uppercase;
  }
  .brand-dot { width: 26px; height: 26px; border-radius: 50%; background: var(--green); }
  .headline {
    left: 30px; top: 206px; font-family: "Orbitron", sans-serif; font-weight: 500;
    font-size: 30px; line-height: 37px; color: #fff; text-transform: uppercase;
  }
  .headline-name {
    left: 30px; top: 332px; font-family: "Montserrat", sans-serif; font-weight: 800;
    font-size: 20px; color: var(--green); text-transform: uppercase; letter-spacing: .3px;
  }
  .tagline-top {
    left: 30px; top: 402px; font-family: "Fira Sans", sans-serif; font-weight: 400;
    font-size: 22px; color: #fff; text-transform: uppercase;
  }
  .tagline-main {
    left: 30px; top: 428px; font-family: "Fira Sans", sans-serif; font-weight: 800;
    font-size: 34px; color: #fff; text-transform: uppercase;
  }
  .section-title {
    font-family: "Fira Sans", sans-serif; font-weight: 800; font-size: 30px;
    line-height: 31px; color: var(--green); text-transform: uppercase;
  }
  .explore { left: 33px; top: 527px; }
  .services-title { left: 449px; top: 604px; }
  .about {
    left: 33px; top: 591px; width: 373px; font-size: 14.2px; line-height: 18.3px;
    text-align: justify; color: #222;
  }
  .about p + p { margin-top: 18px; }
  .services { left: 449px; top: 680px; list-style: none; }
  .services li {
    display: flex; align-items: center; gap: 11px; height: 33.2px;
    font-family: "Fira Sans", sans-serif; font-weight: 700; font-size: 24px;
    color: var(--navy); text-transform: uppercase;
  }
  .tick { width: 21px; height: 21px; flex: none; }
  .callout {
    border: 2px dashed var(--green); border-radius: 8px; height: 102px;
    display: flex; flex-direction: column; justify-content: center; align-items: center;
    text-align: center;
  }
  .callout-hours { left: 33px; top: 874px; width: 365px; }
  .callout-hours strong {
    font-family: "Montserrat", sans-serif; font-weight: 800; font-size: 36px;
    line-height: 38px; color: var(--navy); text-transform: uppercase;
  }
  .callout-vans { left: 441px; top: 874px; width: 364px; border-color: var(--navy); }
  .callout-vans strong {
    font-family: "Montserrat", sans-serif; font-weight: 800; font-size: 22px;
    color: var(--green); text-transform: uppercase; letter-spacing: .5px;
  }
  .callout-vans span { font-size: 16px; line-height: 21px; color: var(--navy); }
  .phone {
    left: 26px; top: 1025px; display: flex; align-items: center; gap: 10px;
    font-family: "Montserrat", sans-serif; font-weight: 800; font-size: 37px; color: #111;
  }
  .phone svg { width: 38px; height: 38px; }
  .contact {
    left: 430px; top: 1030px; font-size: 13px; line-height: 18px; color: #fff;
  }
  .contact-row { display: flex; align-items: center; gap: 6px; white-space: nowrap; }
  .contact-row svg { width: 11px; height: 11px; flex: none; }
</style>
</head>
<body>
<main class="flyer">
  <svg class="flyer-shapes" width="842" height="1090" viewBox="0 0 842 1090" aria-hidden="false">
    <defs>
      <linearGradient id="lightPanel" x1="0" y1="0" x2="1" y2="1">
        <stop offset="0" stop-color="#ffffff"/>
        <stop offset="1" stop-color="#e9eaec"/>
      </linearGradient>
      <linearGradient id="photoTone" x1="0" y1="0" x2="0" y2="1">
        <stop offset="0" stop-color="#d9d3c6"/>
        <stop offset=".5" stop-color="#7a8270"/>
        <stop offset="1" stop-color="#b78f5e"/>
      </linearGradient>
      <linearGradient id="vanTone" x1="0" y1="0" x2="1" y2="0">
        <stop offset="0" stop-color="#f4f5f6"/>
        <stop offset=".6" stop-color="#dfe1e4"/>
        <stop offset="1" stop-color="#5b5a8a"/>
      </linearGradient>
    </defs>
    <rect class="content-bg" x="0" y="494" width="842" height="511" fill="url(#lightPanel)"/>
    <rect class="services-bg" x="420" y="586" width="422" height="419" fill="#eceef0"/>
    <polygon class="navy-wedge" points="606,0 606,140 420,181 470,140" fill="var(--navy)"/>
    <rect class="navy-band" x="0" y="181" width="600" height="203" fill="var(--navy)"/>
    <circle class="navy-ring" cx="602" cy="270" r="190" fill="var(--navy)"/>
    <rect class="ring-trim" x="606" y="0" width="236" height="80" fill="#fff"/>
    <circle class="photo-frame" cx="602" cy="270" r="158" fill="#fff"/>
    <g role="img" aria-label="Smiling courier in cap and polo holding a branded cardboard parcel">
      <circle cx="606" cy="270" r="150" fill="url(#photoTone)"/>
    </g>
    <polygon class="green-band" points="0,384 434,384 494,494 0,494" fill="var(--green)"/>
    <g role="img" aria-label="White delivery van with navy and green brand livery">
      <path d="M409,440 Q430,395 500,384 L842,382 L842,586 L409,586 Z" fill="url(#vanTone)"/>
    </g>
    <polygon class="footer-green" points="0,1005 382,1005 418,1090 0,1090" fill="var(--green)"/>
    <polygon class="footer-navy" points="382,1005 842,1005 842,1090 418,1090" fill="var(--navy)"/>
  </svg>

  <div class="abs brand"><span class="brand-dot"></span>Harbor Parcelworks</div>

  <h1 class="abs headline">Fast reliable and<br>friendly courier<br>in the town!</h1>
  <div class="abs headline-name">Harbor Parcelworks</div>

  <div class="abs tagline-top">Same day &amp; next day couriers</div>
  <div class="abs tagline-main">Dedicated to deliver</div>

  <h2 class="abs section-title explore">Explore what<br>we are doing better</h2>
  <div class="abs about">
    <p>Lorem Ipsum is simply dummy text of the printing and typesetting industry. Lorem Ipsum has been the industry's standard dummy text ever since the 1500s, when an unknown printer took a galley of type and scrambled it to make a type specimen book. It has survived not only five centuries, but also the leap into electronic typesetting, remaining essentially unchanged.</p>
    <p>It was popularised in the 1960s with the release of Letraset sheets containing Lorem Ipsum passages, and more recently with desktop publishing software like Aldus PageMaker including versions of Lorem Ipsum.</p>
  </div>

  <h2 class="abs section-title services-title">We specialized in<br>following services</h2>
  <ul class="abs services">
    <li><svg class="tick" viewBox="0 0 24 24"><circle cx="12" cy="12" r="10" fill="none" stroke="var(--navy)" stroke-width="2"/><path d="M7 12l4 4 8-9" fill="none" stroke="var(--navy)" stroke-width="2.4"/></svg>Same day deliveries</li>
    <li><svg class="tick" viewBox="0 0 24 24"><circle cx="12" cy="12" r="10" fill="none" stroke="var(--navy)" stroke-width="2"/><path d="M7 12l4 4 8-9" fill="none" stroke="var(--navy)" stroke-width="2.4"/></svg>Next day</li>
    <li><svg class="tick" viewBox="0 0 24 24"><circle cx="12" cy="12" r="10" fill="none" stroke="var(--navy)" stroke-width="2"/><path d="M7 12l4 4 8-9" fill="none" stroke="var(--navy)" stroke-width="2.4"/></svg>Light removals</li>
    <li><svg class="tick" viewBox="0 0 24 24"><circle cx="12" cy="12" r="10" fill="none" stroke="var(--navy)" stroke-width="2"/><path d="M7 12l4 4 8-9" fill="none" stroke="var(--navy)" stroke-width="2.4"/></svg>Industry specialist</li>
    <li><svg class="tick" viewBox="0 0 24 24"><circle cx="12" cy="12" r="10" fill="none" stroke="var(--navy)" stroke-width="2"/><path d="M7 12l4 4 8-9" fill="none" stroke="var(--navy)" stroke-width="2.4"/></svg>Secure &amp; fully insured</li>
  </ul>

  <div class="abs callout callout-hours"><strong>24/7 non<br>stop moving</strong></div>
  <div class="abs callout callout-vans">
    <strong>Our dedicated vans</strong>
    <span>can collect from and deliver<br>to anywhere.</span>
  </div>

  <div class="abs phone">
    <svg viewBox="0 0 24 24"><rect x="3" y="2" width="16" height="20" rx="2" fill="#111"/><path d="M8 9.5a3 3 0 1 1 6 0a3 3 0 1 1-6 0zM6 18c0-3 2.5-4.5 5-4.5s5 1.5 5 4.5z" fill="var(--green)"/><path d="M19 3h4M21 1v4" stroke="#111" stroke-width="1.6"/></svg>
    (123) 456-7890
  </div>

  <div class="abs contact">
    <div class="contact-row"><svg viewBox="0 0 12 12"><path d="M6 11s4-4 4-6.5a4 4 0 0 0-8 0C2 7 6 11 6 11z" fill="none" stroke="var(--green)" stroke-width="1.3"/><circle cx="6" cy="4.5" r="1.3" fill="var(--green)"/></svg>517 NE 46th Lane, Ft. Lauderdale, Florida 33308</div>
    <div class="contact-row"><svg viewBox="0 0 12 12"><rect x="1" y="2.5" width="10" height="7" fill="none" stroke="var(--green)" stroke-width="1.3"/><path d="M1 2.5l5 4 5-4" fill="none" stroke="var(--green)" stroke-width="1.3"/></svg>Harbor618@mailvane.com&nbsp;<svg viewBox="0 0 12 12"><circle cx="6" cy="6" r="5" fill="none" stroke="var(--green)" stroke-width="1.2"/><path d="M1 6h10M6 1c-2.5 3-2.5 7 0 10M6 1c2.5 3 2.5 7 0 10" fill="none" stroke="var(--green)" stroke-width="1"/></svg>www.Harbor618.com</div>
  </div>
</main>
</body>
</html>
```